KVD Insurance - Letterhead

We need a corporate letterhead template (word) and slide show template (PowerPoint) designed for our Insurance Business.
KVD Insurance is in the insurance industry. Please visit our website www.kvdinsurance-example.com
Both templates (word and PowerPoint) must include the KVD logo (attached to this project) and can be very similar in design.
We are after something creative yet professional in design.
Please feel free to ask any questions.

```html
<!DOCTYPE html>
<html lang="en">
<head>
<meta charset="utf-8">
<title>KVD Insurance – Letterhead</title>
<link rel="stylesheet" href="https://fonts.googleapis.com/css2?family=Questrial&display=swap">
<style>
  :root {
    --backdrop: #e9e9e9;
    --paper: #f4f4f4;
    --ink: #1d1d1f;
    --ink-soft: #5a5a5e;
    --rule: #c9c9cc;
    --brand-orange: #e8641b;
    --brand-blue: #1d2a85;
    --brand-yellow: #f2c318;
  }
  * { box-sizing: border-box; margin: 0; padding: 0; }
  html, body {
    width: 1200px;
    height: 936px;
    overflow: hidden;
    background: var(--backdrop);
    font-family: "Questrial", "Century Gothic", sans-serif;
  }
  .letterhead {
    position: absolute;
    left: 290px;
    top: 29px;
    width: 620px;
    height: 877px;
    background: var(--paper);
    box-shadow: 0 2px 10px rgba(0,0,0,0.12);
  }
  .brand {
    position: absolute;
    left: 44px;
    top: 58px;
    display: flex;
    align-items: center;
    gap: 8px;
  }
  .brand-dot {
    width: 14px;
    height: 14px;
    border-radius: 50%;
    background: var(--brand-orange);
  }
  .brand-name {
    font-size: 22px;
    color: var(--ink);
    letter-spacing: 1px;
  }
  .contact {
    position: absolute;
    left: 14px;
    bottom: 26px;
    display: flex;
    align-items: flex-end;
    gap: 14px;
    font-size: 8.5px;
    color: var(--ink-soft);
    line-height: 1.5;
  }
  .contact-list { list-style: none; }
  .contact-list li { display: flex; align-items: center; gap: 5px; }
  .contact-icon { width: 8px; height: 8px; flex: none; }
  .contact-divider {
    width: 1px;
    height: 30px;
    background: var(--rule);
    margin-left: 6px;
  }
  .address { font-style: normal; padding-bottom: 2px; }
  .footer-band {
    position: absolute;
    left: 0;
    right: 0;
    bottom: 0;
    height: 11px;
    display: flex;
    gap: 3px;
  }
  .footer-band-orange { width: 34%; background: var(--brand-orange); }
  .footer-band-blue { flex: 1; background: var(--brand-blue); }
</style>
</head>
<body>
  <main class="letterhead">
    <header class="brand">
      <span class="brand-dot"></span>
      <span class="brand-name">KVD Insurance</span>
    </header>

    <footer class="contact">
      <ul class="contact-list">
        <li>
          <svg class="contact-icon" viewBox="0 0 10 10" aria-hidden="true">
            <circle cx="5" cy="5" r="5" fill="var(--brand-orange)"/>
            <path d="M3.2 2.6l1 1-.5.7a3.5 3.5 0 0 0 1.9 1.9l.7-.5 1 1-.7.8C4.9 7.4 2.6 5.1 2.4 3.3z" fill="#fff"/>
          </svg>
          1300 555 019
        </li>
        <li>
          <svg class="contact-icon" viewBox="0 0 10 10" aria-hidden="true">
            <circle cx="5" cy="5" r="5" fill="var(--brand-yellow)"/>
            <rect x="2.5" y="3.2" width="5" height="3.6" fill="none" stroke="#fff" stroke-width="0.8"/>
            <path d="M2.5 3.2L5 5.2l2.5-2" fill="none" stroke="#fff" stroke-width="0.8"/>
          </svg>
          info@kvdinsurance-example.com
        </li>
        <li>
          <svg class="contact-icon" viewBox="0 0 10 10" aria-hidden="true">
            <circle cx="5" cy="5" r="5" fill="var(--brand-blue)"/>
            <circle cx="5" cy="5" r="2.8" fill="none" stroke="#fff" stroke-width="0.6"/>
            <path d="M2.2 5h5.6M5 2.2c-1.5 1.6-1.5 4 0 5.6M5 2.2c1.5 1.6 1.5 4 0 5.6" fill="none" stroke="#fff" stroke-width="0.6"/>
          </svg>
          www.kvdinsurance-example.com
        </li>
      </ul>
      <span class="contact-divider"></span>
      <address class="address">
        Po Box 418<br>
        Lindale VIC 3990
      </address>
    </footer>

    <div class="footer-band">
      <span class="footer-band-orange"></span>
      <span class="footer-band-blue"></span>
    </div>
  </main>
</body>
</html>
```